Postcard promoting HIPAA services, including training, risk assessments, policies, etc.

I am planning a campaign to medical practices advertising HIPAA services. The primary message to convey is that HIPAA random audits are beginning in early 2016, is your practice ready. I need a full-color front design, 4.25 x 6. The design should convey some sense of urgency, and should be dramatic enough to catch the attention of a busy medical practice.

Target Market(s)

Medical, dental, chiropractic, and counseling practices

Industry/Entity Type

Doctor

Font styles to use
Sans Serif

Requirements
Must have
• Sense of urgency, specific mention of upcoming HIPAA audits, feeling that smaller practices are not exempt.

```html
<!DOCTYPE html>
<html lang="en">
<head>
<meta charset="utf-8">
<title>HIPAA Audit Postcard</title>
<link href="https://fonts.googleapis.com/css2?family=Bebas+Neue&family=Lato:wght@400;700&display=swap" rel="stylesheet">
<style>
  :root {
    --orange: #cf5526;
    --orange-bright: #e06a2e;
    --charcoal: #3a3a3a;
    --ink: #4a4a4a;
    --paper: #f4f4f4;
    --paper-shade: #dcdcdc;
    --stage: #e7e3de;
    --white: #ffffff;
    --muted: #b5b5b5;
  }
  * { box-sizing: border-box; margin: 0; padding: 0; }
  html, body { width: 900px; height: 1200px; overflow: hidden; }
  body { background: var(--stage); position: relative; font-family: "Lato", sans-serif; }

  .card { position: absolute; left: 98px; width: 704px; height: 495px; overflow: hidden;
          background: linear-gradient(180deg, var(--paper) 0%, var(--paper-shade) 100%);
          box-shadow: 0 4px 14px rgba(0,0,0,.25); }
  .card--front { top: 85px; }
  .card--back { top: 635px; }

  .display { font-family: "Bebas Neue", sans-serif; line-height: 1; letter-spacing: .5px; }

  /* front */
  .front-header { position: absolute; left: 0; top: 0; width: 100%; height: 125px; background: var(--charcoal); }
  .front-headline { position: absolute; left: 26px; top: 28px; font-weight: 400; }
  .headline-lead { color: var(--orange-bright); font-size: 37px; }
  .headline-main { color: var(--white); font-size: 40px; margin-top: 3px; }
  .question-tab { position: absolute; left: 0; top: 122px; width: 322px; height: 38px;
                  background: var(--orange); border-radius: 0 14px 14px 0;
                  color: var(--white); font-size: 22px; padding: 5px 0 0 28px; }
  .intro-copy { position: absolute; left: 27px; top: 180px; width: 286px;
                font-size: 13.6px; line-height: 1.4; color: var(--ink); text-align: justify; }
  .hero-photo { position: absolute; left: 374px; top: 45px; width: 316px; height: 277px;
                border: 5px solid var(--orange); border-radius: 28px;
                background: linear-gradient(135deg, #8fd0ef 0%, #2f8fc6 50%, #18456f 100%);
                box-shadow: 0 0 0 4px var(--white); }
  .brand { position: absolute; left: 22px; top: 372px; width: 200px; text-align: center; }
  .brand-mark { display: inline-flex; align-items: center; gap: 10px;
                font-size: 30px; font-weight: 400; color: var(--charcoal); }
  .brand-mark::before { content: ""; width: 18px; height: 18px; background: var(--orange); }
  .brand-tagline { font-size: 9px; color: var(--muted); margin-top: 14px; }
  .contact-call { position: absolute; font-size: 48px; color: var(--charcoal); white-space: nowrap; }
  .contact-call span { color: var(--orange); }
  .contact-web { position: absolute; font-size: 24px; color: var(--charcoal); white-space: nowrap; }
  .card--front .contact-call { left: 249px; top: 348px; }
  .card--front .contact-web { left: 249px; top: 401px; }
  .footer-band { position: absolute; left: 0; bottom: 0; width: 100%; height: 42px;
                 background: var(--orange); border-top: 8px solid var(--charcoal); }

  /* back */
  .back-heading { position: absolute; left: 0; top: 0; width: 372px; height: 125px;
                  padding: 30px 0 0 26px; background: var(--paper); font-weight: 400; }
  .back-heading .headline-main { color: var(--charcoal); }
  .message-panel { position: absolute; left: 0; top: 125px; width: 372px; height: 195px;
                   background: var(--orange); padding: 28px 26px 0 31px;
                   color: var(--white); font-size: 15px; line-height: 1.33; text-align: justify; }
  .back-contact { position: absolute; left: 0; top: 320px; width: 372px; height: 135px; background: var(--paper); }
  .card--back .contact-call { left: 31px; top: 38px; font-size: 37px; }
  .card--back .contact-web { left: 31px; top: 76px; font-size: 18px; }
  .address-divider { position: absolute; left: 372px; top: 0; width: 9px; height: 460px; background: var(--charcoal); }
  .stamp-box { position: absolute; left: 610px; top: 27px; width: 65px; height: 65px; background: #bdbdbd; }
</style>
</head>
<body>

<section class="card card--front">
  <div class="front-header">
    <h1 class="front-headline display">
      <div class="headline-lead">HIPAA Random Audits Are</div>
      <div class="headline-main">Beginning in Early 2016</div>
    </h1>
  </div>
  <div class="question-tab">Is your practice ready?</div>
  <p class="intro-copy">Let's face it - Information security is a scary issue today, with daily breaking news about the latest breach. The market has responded with a dizzying array of expensive products that are hard to understand, and may not really help anyway.</p>
  <div class="hero-photo" role="img" aria-label="Businessman touching a glowing network of connected user icons"></div>
  <div class="brand">
    <div class="brand-mark">Norvexa</div>
    <div class="brand-tagline">Security Advice for Every Practice</div>
  </div>
  <div class="contact-call display"><span>Let's Talk:</span> 555-014-2870</div>
  <div class="contact-web display">Please visit our website at: www.norvexa.com</div>
  <div class="footer-band"></div>
</section>

<section class="card card--back">
  <div class="back-heading display">
    <div class="headline-lead">HIPAA Random Audits Are</div>
    <div class="headline-main">Beginning in Early 2016</div>
  </div>
  <p class="message-panel">At Norvexa, we are the information security trusted advisor for small and medium businesses, helping them to navigate through the increasingly complex world of risk and information security. Regardless of whether your data is in your office, in the cloud, or both, we can help</p>
  <div class="back-contact">
    <div class="contact-call display"><span>Let's Talk:</span> 555-014-2870</div>
    <div class="contact-web display">Please visit our website at: www.norvexa.com</div>
  </div>
  <div class="address-divider"></div>
  <div class="stamp-box"></div>
  <div class="footer-band"></div>
</section>

</body>
</html>
```